new branding The Velvet Sip House

The Velvet Sip House is a Belgian brand of ready to serve mocktails. We're looking for a rebranding of the labels on our bottles (8 different flavours)
Our mocktails are low in sugar, 100% natural and completely alcohol-free. They are also 'ready to serve': gently shake the bottle, serve with ice cubes, finish and your mocktail is ready in no time!
Besides being the ideal aperitif, you can also serve them during brunch or dinner. Thanks to the different flavors, you can pair each mocktail with a dish.
Please visit our website to see the current look&feel: the velvetsiphouse.com - https://thevelvetsiphouse.glimmerfold.com/

Target Market(s)

people looking for a premium alcoholfree alternative - premium market

Industry/Entity Type

Mocktails (our mocktails have unique flavors, it's not the non-alcoholic version of a cocktail)

Colors

Designer to choose colors to be used in the design.

Requirements
Must have
• Our brand should be more visible, more recognizable, bolder, without losing the premium and refined character. Base colors should be white, black and silver. The brand should be put more foward. Keep number concept (every mocktail has its number) Put the ingredients/flavours/combinations a bit more forward. make the brand more confident and mature. The eight bottles should become a family. PREMIUM EXPRESSION
Nice to have
• We want to work with a white label. Ideas for the shape of the label Some ideas for the label: Play with shapes, cut outs, texture and number of labels. We like the frosted look and the combination of print & label . Working with 2 labels gives it more dynamic, not one big block Clean label. Working with a cut out shape, can be the logo or the numbers ? Working with 2 labels makes it easier to create an importance of messages. Working with an organic shape makes it unique and give a natural touch Working with a cut out can give a color pop on the white label The label can have parts coming out of the square shape
Should not have
• No crazy stuff, finishes etc should be feasible/realistic

```html
<!DOCTYPE html>
<html lang="en">
<head>
<meta charset="utf-8">
<title>The Velvet Sip House – Label N01 Basil &amp; Elderflower</title>
<link rel="stylesheet" href="https://fonts.googleapis.com/css2?family=Josefin+Sans:wght@400&family=Montserrat:wght@300;400&display=swap">
<style>
  :root {
    --paper: #ffffff;
    --ink: #1b1718;
    --botanical: #e1e1e3;
    --botanical-soft: #f6f6f7;
    --dieline: #e23a6a;
  }
  html, body {
    margin: 0;
    padding: 0;
    width: 1200px;
    height: 1200px;
    overflow: hidden;
    background: var(--paper);
  }
  .label-sheet {
    display: block;
    width: 1200px;
    height: 1200px;
  }
  .brand-name {
    font-family: "Josefin Sans", sans-serif;
    font-weight: 400;
    fill: var(--ink);
  }
  .label-text {
    font-family: "Montserrat", sans-serif;
    fill: var(--ink);
  }
  .label-text--light { font-weight: 300; }
  .label-text--regular { font-weight: 400; }
  .dieline {
    fill: var(--paper);
    stroke: var(--dieline);
    stroke-width: 1.2;
  }
  .rule { fill: var(--ink); }
</style>
</head>
<body>
<svg class="label-sheet" viewBox="0 0 1200 1200" xmlns="http://www.w3.org/2000/svg">
  <defs>
    <clipPath id="label-shape">
      <path d="M325 76 H859 V333 Q859 356 830 356 H740 Q725 356 725 371 V460 Q727 463 760 464 Q820 468 859 476 Q820 560 755 598 Q845 640 875 773 Q835 783 795 783 Q800 900 767 998 V1013 H800 Q812 1013 812 1028 V1124 H325 Z"/>
    </clipPath>
    <radialGradient id="botanical-tone" cx="0.5" cy="0.5" r="0.55">
      <stop offset="0" stop-color="var(--botanical)"/>
      <stop offset="1" stop-color="var(--botanical-soft)"/>
    </radialGradient>
  </defs>

  <path class="dieline" d="M325 76 H859 V333 Q859 356 830 356 H740 Q725 356 725 371 V460 Q727 463 760 464 Q820 468 859 476 Q820 560 755 598 Q845 640 875 773 Q835 783 795 783 Q800 900 767 998 V1013 H800 Q812 1013 812 1028 V1124 H325 Z"/>

  <g clip-path="url(#label-shape)">
    <rect class="botanical-illustration" role="img" aria-label="Light grey engraved botanical drawing of a lemon branch with leaves"
          x="325" y="340" width="550" height="620" fill="url(#botanical-tone)"/>
  </g>

  <g class="brand-lockup">
    <text class="brand-name" x="392" y="201" font-size="78" textLength="152" lengthAdjust="spacingAndGlyphs">THE</text>
    <text class="brand-name" x="410" y="256" font-size="70" textLength="395" lengthAdjust="spacingAndGlyphs">VELVET SIP</text>
    <text class="brand-name" x="553" y="328" font-size="92" textLength="257" lengthAdjust="spacingAndGlyphs">HOUSE</text>
  </g>

  <g class="flavour-number">
    <text class="label-text label-text--regular" x="547" y="548" font-size="56" textLength="100" lengthAdjust="spacingAndGlyphs">N01</text>
    <rect class="rule" x="537" y="564" width="128" height="2"/>
  </g>

  <g class="flavour-name">
    <text class="label-text label-text--regular" x="438" y="703" font-size="58" textLength="319" lengthAdjust="spacing">BASIL &amp;</text>
    <text class="label-text label-text--regular" x="403" y="765" font-size="34" textLength="390" lengthAdjust="spacing">ELDERFLOWER</text>
  </g>

  <g class="product-facts">
    <text class="label-text label-text--regular" x="488" y="991" font-size="21" textLength="222" lengthAdjust="spacing">FRUIT &amp;HERBS</text>
    <rect class="rule" x="478" y="1004" width="245" height="5"/>
    <text class="label-text label-text--light" x="445" y="1073" font-size="30" textLength="307" lengthAdjust="spacing">ALCOHOL FREE</text>
    <text class="label-text label-text--light" x="435" y="1110" font-size="30" textLength="372" lengthAdjust="spacing">MADE IN BELGIUM</text>
  </g>
</svg>
</body>
</html>
```